ReDesign of Velmarix.example and Velmarix app

Velmarix:

Velmarix aims to be your own personal cloud of profile information with ability to share a part of it with others based on the consumer.

As we visit different sites and buy different products, apply for new jobs, on-board in a company or fill out a basic form at a doctors office, we end up entering the same information again and again albeit with some sections different based on where you are. For example, we enter some basic informaiton “AND” billing address on brindle, vs you enter some basic information “AND” work history on a job site.

What if you created a profile one time and then create justed avatars or keys to a combination of information and at different places use different keys to unlock that specific piece of information.

Use Case 1: Peter Hale applying for a job
Peter goes to task harbor, creates new login, enters where he lives, email, phone, then goes into the most tedious phase of entering work history. He realizes, he also needs to go to Quillrun.example and do the exact same thing and so on on any job site he visits in future.

With Velmarix
Peter goes to Velmarix, updates all his work history, personal information (No SSN or credit card). Now he creates a new “key” called “petersworkrequest” with a cryptic “keycode” and chooses to share personal information + work history for this key. He now goes to any job site to see a “VX” icon. He clicks on that, a pop-up box with key and keycode appears. He ONLY enters petersworkrequset and the keycode he had set, boom, all his work informaiton is auto-populated in task harbor. Immense savings in time for Peter.

Use Case 2: Sharing contact information
Peter meets a beautiful at a bar and thinks he needs to share his personal information but only has a 5 mintue window. He realizes, he has created a key named “Peter42” and has chosen to share his personal information only (no work information). She asks for contact number, he gives her is VX key. She pulls up VX app instead of contact list to add contact, plugs in Peter42 (and a key if peter decides to protect this key with a code) and boom, she has peters phone/email/picture (yes picture), chatterly blog and a contact is automatically created!!!!! She now can really associate this Peter from 8 other Peter’s in the bar!!

Use Case 3: Always stay connected
Peter is bored of Houston and decides to move to LA.He wants a local phone number for people to get in touch with them easily. But now he has to do the painful job of sending all his friends his updated number/contact address. If he had exchanged information with Velmarix key with his friends, his contact information with them is always in sync. TThe Velmarix app is intelligent to know that new information is available for the same profile key. As long as the passcode is the same, that information is automatically updated in the consumers contact list. Next time Peter’s friend picks up the phone, he just need so hit “DIAL”. The correct number is dialed. Along with that, his friends now also have his updated address information which he had shared with the key.

SECURITY
Anytime anyone views your profile using your profile key, you automatically get notified to your registered email address of someone pulling up your profile. If you think it’s suspicious, you can change the access code or set an access code to that public key.

where to go:
Go to http://velmarix.example
Register and play around with different views you can create for your profile with different access codes

Download
Velmarix app from pomelo appshelf or Vantor playshelf. We need a nice look and feel for the app as well.

Target Market(s)

students, careers, hiring companies, anyone starting online presence

Industry/Entity Type

Credit Card

Requirements
Must have

• convey message, simplistic, an app to consume data, always stay updated with friends emails etc
Nice to have
• logo should show a user and multiple facets of user for multiple consumers

```html
<!DOCTYPE html>
<html lang="en">
<head>
<meta charset="utf-8">
<title>Velmarix – Find People</title>
<link rel="stylesheet" href="https://fonts.googleapis.com/css2?family=Maven+Pro:wght@400;500&family=Open+Sans:wght@400&display=swap">
<style>
  :root {
    --screen-grey: #b3b3b3;
    --glow: #f4f4f4;
    --ink: #333333;
    --ink-soft: #3a3a3a;
    --brand-green: #4e9a2c;
    --button-top: #7fc445;
    --button-bottom: #5aa22e;
    --field-top: #7c7c7c;
    --field-mid: #b9b9b9;
    --field-bottom: #a9a9a9;
    --field-edge: #5e5e5e;
    --white: #ffffff;
  }
  html, body {
    margin: 0;
    padding: 0;
    width: 960px;
    height: 1200px;
    overflow: hidden;
  }
  .app-screen {
    position: relative;
    width: 960px;
    height: 1200px;
    background:
      radial-gradient(ellipse 360px 380px at 50% 52%, var(--glow) 0%, rgba(244,244,244,0.55) 40%, rgba(179,179,179,0) 100%),
      var(--screen-grey);
    font-family: "Maven Pro", sans-serif;
  }
  .brand {
    position: absolute;
    top: 390px;
    left: 0;
    width: 100%;
    display: flex;
    justify-content: center;
    align-items: center;
    gap: 12px;
  }
  .brand-mark {
    width: 56px;
    height: 56px;
    border-radius: 8px;
    background: var(--brand-green);
  }
  .brand-name {
    font-size: 36px;
    font-weight: 500;
    color: var(--ink);
    letter-spacing: 0.5px;
  }
  .find-heading {
    position: absolute;
    top: 508px;
    left: 0;
    width: 100%;
    display: flex;
    justify-content: center;
    align-items: center;
    gap: 12px;
    font-size: 24px;
    font-weight: 400;
    color: var(--ink-soft);
  }
  .find-heading svg { width: 28px; height: 28px; }
  .search-form {
    position: absolute;
    top: 578px;
    left: 200px;
    width: 560px;
  }
  .search-field {
    display: block;
    box-sizing: border-box;
    width: 560px;
    height: 54px;
    border-radius: 27px;
    border: 2px solid var(--field-edge);
    background: linear-gradient(to bottom, var(--field-top) 0%, var(--field-mid) 30%, var(--field-bottom) 100%);
    box-shadow: inset 0 3px 4px rgba(0,0,0,0.25);
    color: var(--white);
    font-family: "Open Sans", sans-serif;
    font-size: 14px;
    text-align: center;
    line-height: 50px;
  }
  .find-button {
    display: block;
    margin-top: 16px;
    width: 560px;
    height: 54px;
    border-radius: 27px;
    background: linear-gradient(to bottom, var(--button-top), var(--button-bottom));
    color: var(--white);
    font-family: "Maven Pro", sans-serif;
    font-size: 27px;
    font-weight: 400;
    text-align: center;
    line-height: 54px;
    letter-spacing: 1px;
  }
</style>
</head>
<body>
  <main class="app-screen">
    <header class="brand">
      <div class="brand-mark"></div>
      <span class="brand-name">Velmarix</span>
    </header>

    <h1 class="find-heading" style="margin:0;">
      <svg viewBox="0 0 28 28" aria-hidden="true">
        <circle cx="10.5" cy="10.5" r="7" fill="none" stroke="#3a3a3a" stroke-width="2.6"/>
        <line x1="15.8" y1="15.8" x2="25" y2="25" stroke="#3a3a3a" stroke-width="4" stroke-linecap="round"/>
      </svg>
      <span>Find People</span>
    </h1>

    <div class="search-form">
      <div class="search-field">Search by profil ID</div>
      <div class="find-button">FIND</div>
    </div>
  </main>
</body>
</html>
```